Business cards design on a high standard

We advise clients on insurance and financial matters, since these clients pay for our advice, the design should have a high standard. Our logo should be included. From the colors we are open for everything.

Colors

Designer to choose colors to be used in the design.

```html
<!DOCTYPE html>
<html lang="en">
<head>
<meta charset="utf-8">
<title>Alpine Counsel – Business Cards</title>
<link href="https://fonts.googleapis.com/css2?family=Lato:wght@400;700;900&display=swap" rel="stylesheet">
<style>
  :root{
    --stage:#dedede;
    --red:#d61f26;
    --red-faint:#e04a4f;
    --grey:#9a9a9a;
    --text-grey:#8a8a8a;
    --white:#ffffff;
  }
  *{margin:0;padding:0;box-sizing:border-box}
  html,body{width:1200px;height:960px;overflow:hidden}
  body{background:var(--stage);font-family:'Lato',sans-serif;position:relative}
  .card{
    position:absolute;left:281px;width:655px;height:374px;
    border-radius:26px;overflow:hidden;
    box-shadow:0 4px 3px rgba(0,0,0,.35);
  }
  .card-front{top:80px;background:var(--white)}
  .card-back{top:506px;background:var(--red)}
  .front-art{position:absolute;inset:0;width:655px;height:374px}
  .brand-faint{
    position:absolute;left:490px;top:60px;
    font-weight:900;font-size:130px;letter-spacing:4px;
    color:var(--red-faint);white-space:nowrap;line-height:1;
  }
  .brand{
    font-weight:900;text-transform:uppercase;letter-spacing:2px;line-height:1;
    white-space:nowrap;
  }
  .brand-front{position:absolute;left:64px;top:86px;font-size:34px;color:var(--red)}
  .holder{position:absolute;left:79px;top:184px}
  .holder-name{font-weight:700;font-size:27px;color:var(--red);line-height:1.2}
  .holder-role{font-weight:400;font-size:18px;color:var(--text-grey);margin-top:2px}
  .contacts{position:absolute;left:389px;top:250px;list-style:none}
  .contacts li{
    display:flex;align-items:center;gap:7px;
    color:var(--white);font-size:18px;line-height:24px;
  }
  .contacts svg{width:14px;height:14px;flex:none}
  .brand-back{
    position:absolute;left:0;right:0;top:160px;text-align:center;
    font-size:46px;color:var(--white);
  }
  .back-web{
    position:absolute;left:0;right:0;top:314px;text-align:center;
    color:var(--white);font-size:17px;
  }
</style>
</head>
<body>
  <section class="card card-front">
    <svg class="front-art" viewBox="0 0 655 374" aria-hidden="true">
      <path d="M455 0 Q385 285 30 374 L58 374 Q412 292 492 0 Z" fill="var(--grey)"/>
      <path d="M503 0 Q440 302 72 374 L655 374 L655 0 Z" fill="var(--red)"/>
    </svg>
    <div class="brand-faint" aria-hidden="true">AC</div>
    <div class="brand brand-front">Alpine Counsel</div>
    <div class="holder">
      <div class="holder-name">Marlon Reeve</div>
      <div class="holder-role">CEO &amp; Founder</div>
    </div>
    <ul class="contacts">
      <li>
        <svg viewBox="0 0 14 14"><path d="M3 1 L5 4 L4 5.5 Q5.5 8.5 8.5 10 L10 9 L13 11 L11.5 13 Q5 12 1 3 Z" fill="var(--white)"/></svg>
        (555) 010 2468
      </li>
      <li>
        <svg viewBox="0 0 14 14"><rect x="1" y="3" width="12" height="8" fill="var(--white)"/><path d="M1 3 L7 8 L13 3" fill="none" stroke="var(--red)" stroke-width="1.2"/></svg>
        info@alpinecounsel.com
      </li>
      <li>
        <svg viewBox="0 0 14 14" fill="none" stroke="var(--white)" stroke-width="1.1"><circle cx="7" cy="7" r="6"/><ellipse cx="7" cy="7" rx="2.6" ry="6"/><path d="M1 7 H13 M2 4 H12 M2 10 H12"/></svg>
        www.alpinecounsel.com
      </li>
    </ul>
  </section>

  <section class="card card-back">
    <div class="brand brand-back">Alpine Counsel</div>
    <div class="back-web">www.alpinecounsel.com</div>
  </section>
</body>
</html>
```